Independent Midwife for a positive birth experience needs a vibrant, and elegant business card/logo

I need a business card design with a logo. The logo I would like to be able to use on my website (www.midwifemarisol.com) next to my name.
Therefore the design of the card and logo should suit the colours and design of the website. The title of the website and company is "Marisol Quenby Fairhurst, Midwife" but I'd like to have the business card title to be "Marisol Quenby Fairhurst - Independent Midwife" in bold letters, same script font as in my website.

I provide gold standard midwifery services, one-to-one tailored care, continuity of care throughout the entire pregnancy (antenatal care), the birth and after the birth (postnatal care), home birth, water birth, breast-feeding support, and birth preparation workshops. I also am certified and offer complementary therapies: pregnancy reflexology, rebozo techniques for optimal baby positioning.

The design should incorporate similar colours and style as the website and the "Marisol Quenby Fairhurst - Independent Midwife" on the card should include the same font as in the title of the website, however, in bold. The front of the card should have a logo, title and contact information (phone number 072639518, email marisol.fairhurst@lovantamail.com, website address www.midwifemarisol.com).
The back of the card to include the services I offer.

The logo: use of colour purple (varying shades), should communicate communicate warmth, kindness, compassion. It should convey that I'm a midwife who believes in fostering a trusting relationship with my clients and to provide them with a positive pregnancy and birth experience.

Target Market(s)

Pregnant women or women who are looking to book a private midwife for better birth experience and outcome

Industry/Entity Type

Baby

Contact Information for Business Card

Name and Title on front side together with contact details
The reverse side should have services/packages offered

Font styles to use
Script
Other font styles liked:
• similar script as in my website for name and title, and easy to read font for the rest of the words

Colors
b768aa
a54599
d2a4cc
ffffff

Requirements
Must have
• same font as title of website, but slightly bolder.
• similar design, colours, patterns as in website.
• Also include a gold accent colour somewhere in the design please.
Nice to have
• perhaps a logo of pregnant belly in profile or newborn baby icon

```html
<!DOCTYPE html>
<html lang="en">
<head>
<meta charset="UTF-8">
<title>Marisol Quenby Fairhurst – Independent Midwife Business Card</title>
<link rel="stylesheet" href="https://fonts.googleapis.com/css2?family=Great+Vibes&family=Open+Sans:wght@400;600&display=swap">
<style>
  :root {
    --band-purple: #9a1ee6;
    --lavender: #c99be6;
    --lavender-soft: #b98ad8;
    --ink-white: #ffffff;
    --text-soft: #f0ecf4;
    --gold: #d9a43a;
    --gold-deep: #b8832a;
    --back-dark: #14121a;
    --back-mid: #2a2733;
    --gap: #ffffff;
  }
  * { margin: 0; padding: 0; box-sizing: border-box; }
  html, body {
    width: 1200px; height: 333px; overflow: hidden; background: var(--gap);
  }
  .sheet {
    position: relative; width: 1200px; height: 333px;
    display: flex; justify-content: space-between;
  }
  .card-front, .card-back {
    position: relative; height: 333px; overflow: hidden;
  }
  .card-front { width: 596px; background: #2b2536; }
  .card-back {
    width: 598px;
    background: radial-gradient(ellipse at 50% 40%, var(--back-mid) 0%, #1d1b24 55%, var(--back-dark) 100%);
  }

  /* front */
  .contact-band {
    position: absolute; top: 0; left: 0; width: 100%; height: 45px;
    background: var(--band-purple);
    display: flex; align-items: center; justify-content: space-between;
    padding: 0 20px 0 16px;
    font-family: "Open Sans", Arial, sans-serif; color: var(--ink-white);
  }
  .contact-email { font-size: 14px; }
  .contact-phone { font-size: 20px; letter-spacing: 2px; }

  .hero-photo {
    position: absolute; top: 45px; left: 0; width: 100%; height: 288px;
    background:
      radial-gradient(ellipse 30% 45% at 42% 45%, rgba(235,232,240,0.7) 0%, rgba(200,195,210,0.35) 45%, transparent 75%),
      radial-gradient(ellipse 25% 35% at 15% 35%, rgba(210,205,218,0.5) 0%, transparent 70%),
      linear-gradient(180deg, #3b3546 0%, #5b5070 55%, #6b4f96 100%);
  }

  .brand-mark {
    position: absolute; top: 62px; left: 200px; width: 200px; height: 222px;
    display: flex; flex-direction: column; align-items: center; justify-content: center; gap: 16px;
  }
  .brand-circle {
    width: 130px; height: 130px; border-radius: 50%;
    border: 3px solid var(--ink-white);
  }
  .brand-name {
    font-family: "Open Sans", Arial, sans-serif; font-size: 15px; font-weight: 600;
    line-height: 20px; color: var(--ink-white); text-align: center;
  }

  .certified-seal { position: absolute; top: 56px; left: 474px; }
  .front-web {
    position: absolute; top: 154px; right: 13px;
    font-family: "Open Sans", Arial, sans-serif; font-size: 11px; color: var(--text-soft);
  }
  .front-title {
    position: absolute; bottom: 10px; left: 0; width: 100%; text-align: center;
    font-family: "Great Vibes", cursive; font-size: 29px; font-weight: 400;
    color: var(--ink-white); white-space: nowrap;
  }

  /* back */
  .services-title {
    position: absolute; top: 22px; left: 0; width: 100%; text-align: center;
    font-family: "Great Vibes", cursive; font-size: 46px; color: var(--lavender);
    font-weight: 400;
  }
  .services-list {
    position: absolute; top: 86px; left: 0; width: 100%; list-style: none;
    text-align: center; font-family: "Open Sans", Arial, sans-serif;
    font-size: 15.5px; line-height: 24px; color: var(--text-soft);
  }
  .therapies-heading {
    position: absolute; top: 205px; left: 0; width: 100%; text-align: center;
    font-family: "Open Sans", Arial, sans-serif; font-size: 17px; font-weight: 400;
    color: var(--text-soft);
  }
  .therapies-list {
    position: absolute; top: 244px; left: 0; width: 100%; text-align: center;
    font-family: "Open Sans", Arial, sans-serif; font-size: 15.5px; color: var(--text-soft);
    white-space: nowrap;
  }
  .back-web {
    position: absolute; top: 289px; left: 0; width: 100%; text-align: center;
    font-family: "Open Sans", Arial, sans-serif; font-size: 14.5px; color: var(--lavender-soft);
  }
</style>
</head>
<body>
<main class="sheet">
  <section class="card-front">
    <div class="hero-photo" role="img" aria-label="Soft black and white photo of a newborn baby's feet with a purple tint"></div>
    <header class="contact-band">
      <span class="contact-email">marisol.fairhurst@lovantamail.com</span>
      <span class="contact-phone">072639518</span>
    </header>
    <div class="brand-mark">
      <span class="brand-circle"></span>
      <span class="brand-name">Marisol Quenby<br>Fairhurst</span>
    </div>
    <svg class="certified-seal" width="84" height="84" viewBox="0 0 84 84" aria-label="Certification seal">
      <circle cx="42" cy="42" r="38" fill="var(--gold)"/>
    </svg>
    <span class="front-web">www.midwifemarisol.com</span>
    <h1 class="front-title">Marisol Quenby Fairhurst, Independent Midwife</h1>
  </section>

  <section class="card-back">
    <h2 class="services-title">Midwife Services</h2>
    <ul class="services-list">
      <li>One-to-one tailored care,</li>
      <li>Continuity of care throughout the entire pregnancy (Antenatal Care),</li>
      <li>The birth and after the birth (Postnantal Care),</li>
      <li>Home birth, Water birth, Breast-feeding support,</li>
      <li>Birth preparation workshop.</li>
    </ul>
    <h3 class="therapies-heading">Offer Complementary Therapies :</h3>
    <p class="therapies-list">Pregnancy reflexologi, Rebozo techniques for optimal baby positioning.</p>
    <p class="back-web">www.midwifemarisol.com</p>
  </section>
</main>
</body>
</html>
```